Business Card Design

We are an IT staffing and consulting company providing IT solutions and resources to our clients.

Industry/Entity Type

Business

Contact Information for Business Card

Ramesh Tulavarthi
Vice President

BrightNode Inc
48215 Harrowmere Court Square, suite 700
Larkfield, VA 20198
Direct: 571-555-0193
Mobile: 571-555-0147
Email: Ramesh@brightnodeinc.com
Fax: 703-555-0162
www.brightnodeinc.com

```html
<!DOCTYPE html>
<html lang="en">
<head>
<meta charset="utf-8">
<title>BrightNode Inc – Business Card</title>
<link rel="stylesheet" href="https://fonts.googleapis.com/css2?family=Questrial&family=Source+Sans+3:wght@600&display=swap">
<style>
  :root {
    --backdrop: #6e4e38;
    --card: #ffffff;
    --brand-red: #b3202a;
    --ink: #1b1b1b;
    --shadow: rgba(0, 0, 0, 0.35);
  }
  * { margin: 0; padding: 0; box-sizing: border-box; }
  html, body { width: 1200px; height: 1000px; overflow: hidden; }
  body {
    background: var(--backdrop);
    position: relative;
    font-family: "Questrial", sans-serif;
    color: var(--ink);
  }
  .card {
    position: absolute;
    left: 265px;
    width: 665px;
    height: 397px;
    background: var(--card);
    box-shadow: 0 4px 10px var(--shadow);
  }
  .card--front { top: 73px; }
  .card--back { top: 532px; }

  .front-wordmark {
    position: absolute;
    left: 60px;
    top: 178px;
    width: 220px;
    text-align: center;
    font-size: 34px;
    color: var(--brand-red);
  }

  .contact {
    position: absolute;
    left: 333px;
    top: 82px;
    font-size: 16.5px;
    line-height: 1;
  }
  .contact__name {
    font-family: "Source Sans 3", sans-serif;
    font-weight: 600;
    font-size: 20px;
    color: var(--brand-red);
  }
  .contact__title { font-size: 17px; margin-top: 5px; }
  .contact__list { list-style: none; margin-top: 19px; }
  .contact__list li {
    display: flex;
    align-items: center;
    height: 21.5px;
  }
  .contact__icon {
    width: 14px;
    height: 14px;
    margin-right: 8px;
    fill: var(--brand-red);
    flex: none;
  }
  .contact__company { color: var(--brand-red); margin-top: 4px; }
  .contact__address { margin-top: 2px; line-height: 22px; }

  .back-brand {
    position: absolute;
    left: 0;
    right: 0;
    top: 176px;
    display: flex;
    justify-content: center;
    align-items: center;
    gap: 16px;
  }
  .back-brand__dot {
    width: 22px;
    height: 22px;
    border-radius: 50%;
    background: var(--brand-red);
  }
  .back-brand__name { font-size: 50px; color: var(--ink); }

  .back-url {
    position: absolute;
    left: 0;
    right: 0;
    top: 348px;
    text-align: center;
    font-size: 18px;
    letter-spacing: 2.6px;
  }
  .back-url__domain { color: var(--brand-red); }
</style>
</head>
<body>
  <section class="card card--front">
    <div class="front-wordmark">BrightNode</div>

    <div class="contact">
      <div class="contact__name">Ramesh Tulavarthi</div>
      <div class="contact__title">Vice President</div>
      <ul class="contact__list">
        <li>
          <svg class="contact__icon" viewBox="0 0 14 14" aria-hidden="true"><path d="M4 1h6v12H4z M5 2v9h4V2z" fill-rule="evenodd"/></svg>
          571-555-0147
        </li>
        <li>
          <svg class="contact__icon" viewBox="0 0 14 14" aria-hidden="true"><path d="M1 5c0-2 3-3 6-3s6 1 6 3v1h-3V4.5H4V6H1z M3 7h8l1 5H2z"/></svg>
          571-555-0193
        </li>
        <li>
          <svg class="contact__icon" viewBox="0 0 14 14" aria-hidden="true"><path d="M4 1h6v4H4z M1 6h12v5h-2v2H3v-2H1z M4 9v3h6V9z" fill-rule="evenodd"/></svg>
          703-555-0162
        </li>
        <li>
          <svg class="contact__icon" viewBox="0 0 14 14" aria-hidden="true"><path d="M1 3h12v1L7 8 1 4z M1 5.5l6 4 6-4V11H1z"/></svg>
          ramesh@brightnodeinc.com
        </li>
        <li>
          <svg class="contact__icon" viewBox="0 0 14 14" aria-hidden="true"><circle cx="7" cy="7" r="6"/><path d="M1 7h12M7 1v12M3 3.5h8M3 10.5h8" stroke="#fff" stroke-width="0.9" fill="none"/></svg>
          www.brightnodeinc.com
        </li>
      </ul>
      <div class="contact__company">BrightNode Inc</div>
      <div class="contact__address">48215 Harrowmere Court Square,<br>suite 700 Larkfield, VA 20198</div>
    </div>
  </section>

  <section class="card card--back">
    <div class="back-brand">
      <span class="back-brand__dot"></span>
      <span class="back-brand__name">BrightNode</span>
    </div>
    <div class="back-url">www.<span class="back-url__domain">brightnodeinc</span>.com</div>
  </section>
</body>
</html>
```